Young, dynamic furniture company needs a new business card design

We require a new business card design for our modern furniture company which supplies furniture and appliances to the property and development market.
Corvane Furnishing has become one of the leading furniture & appliance suppliers to the property market withing London. With over 10 years experience, we have increased our business to supply not only private landlords and managing agents, but also property developers, housing associations and local councils.
We offer not only a complete range of furniture which includes beds, wardrobes, dining sets and sofas, but also a high quality, full delivery and assembly service to help you with all our furnishing needs.

Target Market(s)

Private landlords, estate agents, letting agents, property management companies

Industry/Entity Type

Business

Contact Information for Business Card

Name,
Title,
Address,
Mobile,
Telephone,
Fax, Website, email address

Font styles to use
Sans Serif

Colors
3176b5
0555a3
85abd2
cfdeed

Requirements
Must have
• All the above information for each of our staff, along with our logo

```html
<!DOCTYPE html>
<html lang="en">
<head>
<meta charset="utf-8">
<title>Corvane Furnishing – Business Card</title>
<link rel="stylesheet" href="https://fonts.googleapis.com/css2?family=Roboto+Condensed:wght@300;400;700&display=swap">
<style>
  :root {
    --blue: #3176b5;
    --blue-deep: #0555a3;
    --blue-soft: #85abd2;
    --blue-pale: #cfdeed;
    --white: #ffffff;
    --ink: #2b2b2b;
    --backdrop: #e9ecef;
  }
  * { box-sizing: border-box; margin: 0; padding: 0; }
  html, body { width: 1200px; height: 900px; overflow: hidden; }
  body {
    background: var(--backdrop);
    font-family: "Roboto Condensed", Arial, sans-serif;
    position: relative;
  }
  .card {
    position: absolute;
    width: 560px;
    height: 320px;
    border-radius: 4px;
    box-shadow: 0 6px 18px rgba(0,0,0,.18);
  }
  .card--front {
    left: 60px; top: 120px;
    background: linear-gradient(135deg, var(--blue) 0%, #2b6eae 55%, var(--blue-deep) 100%);
    color: var(--white);
    display: flex; flex-direction: column; align-items: center; justify-content: center;
    text-align: center;
  }
  .card--back {
    left: 580px; top: 470px;
    background: var(--white);
    display: flex; align-items: flex-end; justify-content: center;
    padding-bottom: 70px;
  }
  .brand { display: flex; align-items: center; justify-content: center; gap: 10px; }
  .brand__square { width: 16px; height: 16px; background: currentColor; flex: none; }
  .brand__name {
    font-weight: 300; font-size: 26px; letter-spacing: .5px; text-transform: uppercase;
    white-space: nowrap;
  }
  .brand__tagline {
    font-weight: 300; font-size: 10px; letter-spacing: 1.5px; text-transform: uppercase;
    margin-top: 3px;
  }
  .card--front .brand__tagline { color: var(--blue-pale); }
  .card--back .brand-block { color: var(--blue-deep); text-align: center; }
  .card--back .brand__tagline { color: var(--ink); }
  .address { font-size: 14px; font-weight: 400; margin-top: 20px; white-space: nowrap; }
  .divider {
    width: 260px; height: 1px; margin: 10px 0;
    background: linear-gradient(90deg, transparent, var(--blue-pale), transparent);
  }
  .person__name { font-size: 19px; font-weight: 700; letter-spacing: .5px; text-transform: uppercase; }
  .person__title { font-size: 11px; font-weight: 400; letter-spacing: 1px; text-transform: uppercase; color: var(--blue-pale); }
  .contacts { display: flex; flex-direction: column; gap: 6px; font-size: 13px; }
  .contacts__row { display: flex; gap: 16px; justify-content: center; }
  .contact { display: flex; align-items: center; gap: 5px; white-space: nowrap; }
  .contact svg { width: 12px; height: 12px; flex: none; }
</style>
</head>
<body>

  <section class="card card--front" aria-label="Business card front">
    <div class="brand-block">
      <div class="brand">
        <span class="brand__square"></span>
        <span class="brand__name">Corvane Furnishing</span>
      </div>
      <div class="brand__tagline">Trade Furniture Solutions</div>
    </div>

    <p class="address">2480 Elm Row, Suite 200, City, State, Zip Code</p>
    <div class="divider"></div>

    <div class="person">
      <div class="person__name">Daniel Hartley</div>
      <div class="person__title">Manager</div>
    </div>
    <div class="divider"></div>

    <div class="contacts">
      <div class="contacts__row">
        <span class="contact">
          <svg viewBox="0 0 12 12"><rect width="12" height="12" rx="2" fill="#fff"/><path d="M3.5 2.5l1.5 0 .6 2-1 .7a5 5 0 0 0 2.2 2.2l.7-1 2 .6 0 1.5c-3.5.3-6.3-2.5-6-6z" fill="#3176b5"/></svg>
          0770-4812-5093
        </span>
        <span class="contact">
          <svg viewBox="0 0 12 12"><rect width="12" height="12" rx="2" fill="#fff"/><rect x="4" y="2" width="4" height="8" rx="1" fill="#3176b5"/></svg>
          0713-6620-4418
        </span>
      </div>
      <div class="contacts__row">
        <span class="contact">
          <svg viewBox="0 0 12 12"><rect width="12" height="12" rx="2" fill="#fff"/><rect x="2.5" y="3.5" width="7" height="5" fill="none" stroke="#3176b5"/><path d="M2.5 3.5l3.5 3 3.5-3" fill="none" stroke="#3176b5"/></svg>
          dhartley@mail.com
        </span>
        <span class="contact">
          <svg viewBox="0 0 12 12"><rect width="12" height="12" rx="2" fill="#fff"/><circle cx="6" cy="6" r="3.5" fill="none" stroke="#3176b5"/><path d="M2.5 6h7M6 2.5v7" stroke="#3176b5" stroke-width=".8"/></svg>
          corvane-furnishing.com
        </span>
      </div>
    </div>
  </section>

  <section class="card card--back" aria-label="Business card back">
    <div class="brand-block">
      <div class="brand">
        <span class="brand__square"></span>
        <span class="brand__name">Corvane Furnishing</span>
      </div>
      <div class="brand__tagline">Trade Furniture Solutions</div>
    </div>
  </section>

</body>
</html>
```